Book Title: “Ember: Road of Quiet Dawn” Please see the attachment “Text on the cover”.

Book Cover Design Instructions: This book is meant for people of all religions and nationalities. Therefore, on the cover, there should be no mosque or an object specific to any religion. The primary emphasis should be on the "unconditional love of God." Therefore, use universal symbols of love. The second priority themes could be Sufism, Peace, and self-improvement. Rest is your imagination. Please also see the attachment: 'Book description and author's Bio.'
This book has the potential to be a best seller. Please do a good job.
What Book Cover Formats are required: A designer should submit cover designs in three formats: (1) eBook, (2) Paperback, and (3) Hardback. These books will be published on Velmora PBX.
Format requirements for eBooks are available from: https://pbx.velmora-press.example/en_US/help/topic/R731928405.
You can find paperback and hardback cover measurements from: https://pbx.velmora-press.example/en_US/cover-calculator
• To complete the project, all three formats should be accepted by Velmora PBX.
• The book interior trim size is 6.14 X 9.21 inches.
• Interior Type: Premium color.
• No bleed.
• I do not upload barcode. So, the back cover should have room for Velmora to print the barcode.
• Number of pages 126.
Compensation for the designer: After selecting one designer, I will increase the amount by $200 on Artlumo to compensate for three deliverables.
Follow-up of the Project:
After the book is published, I may need minor revisions. For example, the number of pages may change. Therefore, I will need the same design in revised sizes. In that case, I will pay $25 for each revision. For example, if the number of pages changes, I will need a different spine for paperback and hardback, then I will pay the artist $25 + $25 = $50 for both designs.
List of Enclosers:
1. Text on the cover.
2. Book description and author's Bio for the back cover.
3. Later, I will upload my picture for the book's back cover.

Target Market(s)

Any adult

Industry/Entity Type

Any industry

Requirements
Must have
• Three Deliverables

```html
<!DOCTYPE html>
<html lang="en">
<head>
<meta charset="utf-8">
<title>Ember: Road of Quiet Dawn — Wraparound Cover</title>
<link rel="stylesheet" href="https://fonts.googleapis.com/css2?family=Playfair+Display:ital,wght@0,500;0,700;1,400&family=Rubik:wght@400;500;600&display=swap">
<style>
  :root {
    --stage: #d8d8da;
    --ember-orange: #d9531b;
    --ink: #1b120c;
    --glow-light: #fbeed6;
    --glow-mid: #eab77a;
    --warm-amber: #c97a3a;
    --deep-rust: #7a3512;
    --back-top: #f1c9a0;
    --back-mid: #d9915a;
    --back-low: #6e2c10;
    --spine-light: #e8b07a;
    --spine-dark: #b96a34;
    --barcode-zone: #ffffff;
  }
  * { box-sizing: border-box; margin: 0; padding: 0; }
  html, body {
    width: 693px; height: 1200px; overflow: hidden;
    background: var(--stage);
  }
  .stage {
    width: 693px; height: 1200px;
    display: flex; align-items: center; justify-content: center;
  }
  .wraparound {
    display: flex;
    width: 654px; height: 465px;
    box-shadow: 0 8px 24px rgba(0,0,0,.2);
  }

  /* ---------- Back cover ---------- */
  .back-cover {
    position: relative;
    width: 310px; height: 465px;
    padding: 26px 18px 0 18px;
    background: linear-gradient(180deg, var(--back-top) 0%, #eab486 35%, var(--back-mid) 62%, var(--back-low) 100%);
    color: var(--ink);
    overflow: hidden;
  }
  .back-title {
    font-family: "Playfair Display", serif; font-weight: 500;
    font-size: 19px; line-height: 1.1;
  }
  .back-title .series {
    color: var(--ember-orange); font-weight: 700;
  }
  .back-subtitle {
    font-family: "Rubik", sans-serif; font-weight: 600;
    font-size: 6.6px; letter-spacing: .1px; text-transform: uppercase;
    margin: 2px 0 8px;
  }
  .blurb p, .blurb li {
    font-family: "Rubik", sans-serif; font-weight: 400;
    font-size: 6.1px; line-height: 1.42;
  }
  .blurb p { margin-bottom: 5px; }
  .questions {
    margin: 0 0 5px 14px;
  }
  .questions li {
    font-family: "Playfair Display", serif; font-style: italic;
    font-size: 6.3px; margin-bottom: 2px;
  }
  .author-block {
    position: absolute; left: 18px; top: 360px; right: 18px;
    display: flex; gap: 10px; align-items: flex-start;
  }
  .author-photo {
    width: 44px; height: 52px; flex: none;
    border: 0.8px solid var(--ink);
    margin-top: 10px;
  }
  .author-name-back {
    font-family: "Playfair Display", serif; font-weight: 500;
    font-size: 9px; margin-bottom: 2px;
  }
  .author-bio {
    font-family: "Rubik", sans-serif; font-size: 6px; line-height: 1.4;
  }
  .barcode-zone {
    position: absolute; right: 20px; bottom: 20px;
    width: 76px; height: 46px;
    background: var(--barcode-zone);
  }

  /* ---------- Spine ---------- */
  .spine {
    position: relative;
    width: 34px; height: 465px;
    background: linear-gradient(90deg, var(--spine-dark) 0%, var(--spine-light) 45%, var(--spine-dark) 100%);
    display: flex; flex-direction: column; justify-content: space-between; align-items: center;
    padding: 22px 0 30px;
    writing-mode: vertical-rl;
    color: var(--ink);
  }
  .spine-title {
    font-family: "Playfair Display", serif; font-weight: 500;
    font-size: 10.5px; white-space: nowrap;
  }
  .spine-title .series { color: var(--ember-orange); font-weight: 700; }
  .spine-author {
    font-family: "Playfair Display", serif; font-weight: 500;
    font-size: 10px; white-space: nowrap;
  }

  /* ---------- Front cover ---------- */
  .front-cover {
    position: relative;
    width: 310px; height: 465px;
    overflow: hidden;
    background:
      radial-gradient(ellipse 60% 55% at 50% 42%, var(--glow-light) 0%, var(--glow-mid) 45%, rgba(201,122,58,0) 80%),
      linear-gradient(180deg, #e2a76a 0%, var(--warm-amber) 55%, var(--deep-rust) 100%);
    text-align: center;
  }
  .series-word {
    position: absolute; top: 22px; left: 0; right: 0;
    font-family: "Playfair Display", serif; font-weight: 700;
    font-size: 58px; letter-spacing: 1px; line-height: 1;
    color: var(--ember-orange);
    text-shadow: 0 1px 2px rgba(90,30,0,.25);
  }
  .main-title {
    position: absolute; top: 84px; left: 0; right: 0;
    font-family: "Playfair Display", serif; font-weight: 700;
    font-size: 35px; line-height: 1.02;
    color: var(--ink);
  }
  .subtitle {
    position: absolute; top: 172px; left: 0; right: 0;
    font-family: "Rubik", sans-serif; font-weight: 500;
    font-size: 13px; line-height: 1.3;
    color: var(--ink);
  }
  .cover-art {
    position: absolute; left: 55px; top: 236px;
    width: 200px; height: 168px;
    border-radius: 50% 50% 46% 46%;
    background:
      radial-gradient(circle at 50% 38%, #fff4d8 0%, #f4cf85 18%, rgba(138,154,58,.75) 32%, rgba(190,110,70,.9) 55%, rgba(150,75,40,0) 78%);
  }
  .author {
    position: absolute; bottom: 20px; left: 0; right: 0;
    font-family: "Playfair Display", serif; font-weight: 500;
    font-size: 17px; color: var(--ink);
  }
</style>
</head>
<body>
  <main class="stage">
    <div class="wraparound">

      <section class="back-cover">
        <h2 class="back-title"><span class="series">EMBER:</span>Road of Quiet Dawn</h2>
        <p class="back-subtitle">Guide to Cultivating Inner Peace and Mindful Living</p>
        <div class="blurb">
          <p>This book intricately intertwines the diverse teachings of Sufism with the deep wisdom of the Quran to create a comprehensive roadmap for personal spiritual growth. The reader has a chance to experience firsthand the profound peace and boundless love Sufis have cherished for centuries. This book addresses the following critical questions:</p>
          <ol class="questions">
            <li>How can one unconditionally love God? It is the greatest of all kinds of love that ignites a profound and transformative spiritual journey.</li>
            <li>How to feel the love of God, which can bring immense peace and contentment.</li>
            <li>How to unconditionally love yourself, which nurtures personal growth and harmony.</li>
            <li>What is the most effective way to respond to life's critical crises to reduce suffering and expedite recovery?</li>
          </ol>
          <p>This book also explores the faith's overwhelming emphasis on avoiding Zulm (oppression and injustice) because the Quran mentions the word Zulm an astounding 291 times. Avoiding Zulm in all human interactions should be the top priority for every believer. The Prophet (PBUH) did not just preach peace and love. He gave us a practical example when he took over as a ruler of Medina without bloodshed. He did not inherit power through the dynasty, and Medina was multi-religious. Arguably, it was history's first large-scale peaceful transfer of power.</p>
          <p>Similarly, he signed the Treaty of Hudaybia with the staunchest enemy, employing an unprecedented peaceful strategy to nonviolently end a bitter war that had claimed hundreds of lives.</p>
          <p>The highlight of this book is that it points to the methodology to acquire a fully satisfied and contented soul (<em>Nafs-e-Mutma'inna</em>) in practical steps, which is the goal of every Sufi wayfarer.</p>
        </div>
        <div class="author-block">
          <div class="author-photo" role="img" aria-label="Space reserved for the author's portrait"></div>
          <div>
            <p class="author-name-back">Dr. Idris Halvani</p>
            <p class="author-bio">Dr. Halvani holds a Master's in Physics and a Master's in Computer Science and worked as a Software Engineer. He earned his Ph.D. in Islamic Studies. He was one of the founders of a mosque in Virginia.</p>
          </div>
        </div>
        <div class="barcode-zone" aria-label="Space reserved for the printer's barcode"></div>
      </section>

      <section class="spine">
        <p class="spine-title"><span class="series">EMBER:</span>Road of Quiet Dawn</p>
        <p class="spine-author">Dr. Idris Halvani</p>
      </section>

      <section class="front-cover">
        <h1 class="series-word">EMBER</h1>
        <h2 class="main-title">Road of Quiet<br>Dawn</h2>
        <p class="subtitle">Guide to Cultivating Inner Peace<br>and Mindful Living</p>
        <div class="cover-art" role="img" aria-label="Photograph of cupped hands holding a small glowing tree in warm golden light"></div>
        <p class="author">Dr. Idris Halvani</p>
      </section>

    </div>
  </main>
</body>
</html>
```